Printing company needs stellar web site!

We need a website for a printing company based in Atlanta, Georgia, USA. Our company is 26 years old and just this year did a logo and branding refresh. Now we need our website to be refreshed as well.

Please see the attached source files for our new logo and stationary design.

Industry/Entity Type

Printing

```html
<!DOCTYPE html>
<html lang="en">
<head>
<meta charset="utf-8">
<title>Inkvale – Printing Solutions</title>
<link rel="stylesheet" href="https://fonts.googleapis.com/css2?family=Lato:wght@400;700;900&family=Oswald:wght@500;600&family=Open+Sans:wght@400;600&display=swap">
<style>
:root{
  --blue:#1565b4;
  --blue-dark:#0b4fa0;
  --ink:#1b1b1b;
  --text:#333;
  --cyan:#00b6ee;
  --magenta:#e91c6d;
  --green:#74c21c;
  --purple:#5a44b0;
  --light:#f7f7f7;
  --grey:#e6e6e6;
  --footer:#2c2c2c;
  --footer-bar:#222;
  --footer-text:#d8d8d8;
}
*{margin:0;padding:0;box-sizing:border-box}
html,body{width:753px;height:1200px;overflow:hidden;background:#fff}
body{position:relative;font-family:"Lato",sans-serif;color:var(--text)}
.abs{position:absolute}

.brand{left:0;width:753px;top:18px;text-align:center}
.brand-row{display:inline-flex;align-items:center;gap:8px}
.brand-mark{width:28px;height:28px;border-radius:50%;background:var(--blue)}
.brand-name{font-family:"Oswald",sans-serif;font-weight:600;font-size:29px;letter-spacing:1px;color:var(--blue);line-height:30px}
.tagline{font-family:"Open Sans",sans-serif;font-size:6.4px;color:var(--blue);margin-top:2px;margin-left:40px}
.header-rule{left:165px;width:423px;top:64px;height:1px;background:linear-gradient(90deg,transparent,#cfcfcf,transparent)}
.nav{left:0;width:753px;top:79px;display:flex;justify-content:center;gap:16px;font-family:"Open Sans",sans-serif;font-size:11.2px;color:var(--ink)}
.nav a{color:inherit;text-decoration:none;padding-bottom:4px}
.nav a.active{border-bottom:2px solid var(--blue)}

.hero{left:0;top:106px;width:753px;height:244px;background:linear-gradient(120deg,#8fd6e0 0%,#f2f2f2 22%,#e9117a 38%,#f6d400 50%,#1b2b55 62%,#2a9fd8 74%,#e4e4e4 100%)}
.hero-caption{left:250px;top:286px;width:252px;height:64px;background:rgba(70,70,70,.55);color:#fff;font-family:"Oswald",sans-serif;font-weight:500;font-size:21px;line-height:25px;text-align:center;padding-top:7px;letter-spacing:.3px}

.intro{left:0;top:350px;width:753px;height:348px;background:var(--light)}
.badge{left:333px;top:368px;width:88px;height:28px;border-radius:14px;background:var(--blue);color:#fff;font-size:17px;text-align:center;line-height:28px}
.badge:after{content:"";position:absolute;left:38px;bottom:-6px;border:6px solid transparent;border-top-color:var(--blue);border-bottom:0}
.intro-title{left:0;width:753px;top:397px;text-align:center;font-weight:900;font-size:34px;color:var(--ink);line-height:40px;letter-spacing:1px}
.intro-sub{left:0;width:753px;top:433px;text-align:center;font-weight:900;font-size:23px;color:var(--ink);letter-spacing:.5px}

.service{top:476px;width:126px;height:188px;color:#fff;text-align:center}
.service-title{font-family:"Oswald",sans-serif;font-weight:500;font-size:15px;line-height:16px;padding-top:4px;height:38px}
.service-photo{margin:3px -3px 0;height:74px;border:2px solid #fff;box-shadow:0 1px 3px rgba(0,0,0,.3)}
.service-text{font-size:8px;line-height:11.5px;padding:6px 6px 0}
.service-btn{display:block;width:47px;height:19px;margin:7px auto 0;background:#fff;font-size:8px;line-height:19px}
.s-cyan{left:86px;background:var(--cyan)} .s-cyan .service-btn{color:var(--cyan)}
.s-mag{left:238px;background:var(--magenta)} .s-mag .service-btn{color:var(--magenta)}
.s-green{left:389px;background:var(--green)} .s-green .service-btn{color:var(--green)}
.s-purple{left:540px;background:var(--purple)} .s-purple .service-btn{color:var(--purple)}

.specialty-band{left:0;top:698px;width:753px;height:220px;background:var(--grey)}
.specialty-title{left:82px;top:719px;font-family:"Open Sans",sans-serif;font-weight:600;font-size:17px;color:var(--ink)}
.specialty-text{left:82px;top:748px;width:280px;font-size:8.2px;line-height:12.3px;color:#222}
.ticks{top:823px;list-style:none;font-size:8.2px;color:#222}
.ticks li{height:17.6px;display:flex;align-items:center;gap:8px}
.ticks svg{flex:none}
.divider{left:387px;top:728px;width:1px;height:160px;background:#d2d2d2}

.tabs{left:418px;top:724px;display:flex;gap:3px}
.tab{height:27px;padding:0 14px;background:#ececec;border:1px solid #d5d5d5;border-bottom:0;font-size:8px;line-height:27px;color:#555;letter-spacing:.3px}
.tab.on{background:#fff}
.news{left:418px;top:751px;width:252px;height:135px;background:#fff;border:1px solid #ddd}
.news-photo{left:14px;top:26px;width:88px;height:88px;border:3px solid var(--blue);background:linear-gradient(135deg,#d8dde0,#8fb9d6 50%,#f0a050)}
.news-date{left:116px;top:27px;font-size:7.5px;font-weight:700;color:var(--cyan)}
.news-title{left:116px;top:36px;font-size:19px;line-height:21px;color:var(--ink);width:130px}
.news-text{left:116px;top:83px;width:130px;font-size:8px;line-height:11.5px;color:#666}

.partners{left:0;top:938px;width:753px;display:flex;justify-content:center;gap:34px;font-size:18px;color:#666}
.partner{display:flex;align-items:center;gap:6px}
.partner i{display:block;width:14px;height:14px;border-radius:50%;background:#888}

.footer{left:0;top:940px;width:753px;height:260px;background:var(--footer)}
.swoosh{left:0;top:918px}
.f-col{top:1052px;color:var(--footer-text);font-size:7.6px}
.f-head{font-size:9.6px;font-weight:700;color:#fff;padding-bottom:6px;border-bottom:1px solid #444;margin-bottom:8px}
.f-links{list-style:none}
.f-links li{height:18.3px}
.f-links li:before{content:"›";margin-right:6px}
.contact-row{display:flex;gap:10px;align-items:flex-start;margin-bottom:9px}
.contact-row svg{flex:none}
.contact-row b{font-size:9px;font-weight:700;color:#fff}
.map{width:127px;height:76px;border:2px solid #777;background:linear-gradient(135deg,#e9dcc0,#b9d3e6 55%,#f1c46a)}
.field{width:127px;height:19px;border-radius:2px;background:#444;margin-top:7px;padding-left:7px;font-style:italic;font-size:7.4px;line-height:19px;color:#ddd}
.submit{width:47px;height:15px;margin-top:12px;background:var(--blue);color:#fff;font-weight:700;font-size:8.6px;text-align:center;line-height:15px;border-radius:1px}
.bar{left:0;top:1174px;width:753px;height:26px;background:var(--footer-bar)}
.copyright{left:83px;top:1183px;font-size:7.6px;color:#ccc}
.social{left:588px;top:1181px;display:flex;gap:11px}
.social span{display:block;width:12px;height:12px;border-radius:50%;background:#ddd}
</style>
</head>
<body>

<header>
  <div class="abs brand">
    <div class="brand-row"><span class="brand-mark"></span><span class="brand-name">INKVALE</span></div>
    <div class="tagline">OUTSTANDING SERVICE • QUALITY PRODUCT • COMPETITIVE PRICING.</div>
  </div>
  <div class="abs header-rule"></div>
  <nav class="abs nav">
    <a class="active" href="#">HOME</a><a href="#">ABOUT US</a><a href="#">OUR SERVICES</a><a href="#">SUPPORT</a><a href="#">BLOG</a><a href="#">CONTACT</a>
  </nav>
</header>

<section>
  <div class="abs hero" role="img" aria-label="Colour calibration swatches on a printed proof sheet under a magnifying loupe"></div>
  <div class="abs hero-caption">ALL TYPES OF<br>PRINTING SOLUTIONS</div>
</section>

<section>
  <div class="abs intro"></div>
  <div class="abs badge">26 years</div>
  <h1 class="abs intro-title">OF PRINTING</h1>
  <h2 class="abs intro-sub">EXPERIENCE!</h2>

  <article class="abs service s-cyan">
    <div class="service-title">ENVELOPE<br>PRINTING</div>
    <div class="service-photo" role="img" aria-label="Technician operating a printing press control panel" style="background:linear-gradient(90deg,#c8ccd2,#5a6f95)"></div>
    <p class="service-text">Lorem ipsum dolor sit amet, consectetur adipiscing elit. estibulum vitae vulputate risus.</p>
    <span class="service-btn">More</span>
  </article>
  <article class="abs service s-mag">
    <div class="service-title">PAD<br>PRINTING</div>
    <div class="service-photo" role="img" aria-label="Colourful printed sheets running through press rollers" style="background:linear-gradient(180deg,#3a3a3a,#d83a6a 50%,#e6c23a)"></div>
    <p class="service-text">Lorem ipsum dolor sit amet, consectetur adipiscing elit. estibulum vitae vulputate risus.</p>
    <span class="service-btn">More</span>
  </article>
  <article class="abs service s-green">
    <div class="service-title">CATALOG<br>PRINTING</div>
    <div class="service-photo" role="img" aria-label="Row of coloured ink cartridges inside a printer" style="background:linear-gradient(90deg,#2b2b2b,#3aa0c8 40%,#c83a8a 70%,#2b2b2b)"></div>
    <p class="service-text">Lorem ipsum dolor sit amet, consectetur adipiscing elit. estibulum vitae vulputate risus.</p>
    <span class="service-btn">More</span>
  </article>
  <article class="abs service s-purple">
    <div class="service-title">REAL 3D<br>PRINTING</div>
    <div class="service-photo" role="img" aria-label="Red printed rolls on a large format press" style="background:linear-gradient(180deg,#4a4a55,#b52a3a 60%,#3a2a2a)"></div>
    <p class="service-text">Lorem ipsum dolor sit amet, consectetur adipiscing elit. estibulum vitae vulputate risus.</p>
    <span class="service-btn">More</span>
  </article>
</section>

<section>
  <div class="abs specialty-band"></div>
  <h3 class="abs specialty-title">Our Specialty</h3>
  <p class="abs specialty-text">Quisque magna orci, sagittis ac eros at, consectetur faucibus&nbsp; Pellentesque fermentum viverra commodo. Praesent fringilla et sem eu congue. Donec varius facilisis consequat. Suspendisse semper eu velit a adipisc&nbsp; Phasellus cursus, magna ac sagittis ultricies, ipsum quam gravida magna&nbsp; imperdiet erat ligula id leo. In a neque pretium, porta arcu eget, laoreet arcu.</p>
  <ul class="abs ticks" style="left:82px">
    <li><svg width="8" height="8"><circle cx="4" cy="4" r="4" fill="#1565b4"/><path d="M3 2.2 5 4 3 5.8" stroke="#fff" stroke-width="1" fill="none"/></svg>Lorem ipsum dolor sit amet</li>
    <li><svg width="8" height="8"><circle cx="4" cy="4" r="4" fill="#1565b4"/><path d="M3 2.2 5 4 3 5.8" stroke="#fff" stroke-width="1" fill="none"/></svg>Consectetuer adipiscing</li>
    <li><svg width="8" height="8"><circle cx="4" cy="4" r="4" fill="#1565b4"/><path d="M3 2.2 5 4 3 5.8" stroke="#fff" stroke-width="1" fill="none"/></svg>Pt wisi enim ad</li>
    <li><svg width="8" height="8"><circle cx="4" cy="4" r="4" fill="#1565b4"/><path d="M3 2.2 5 4 3 5.8" stroke="#fff" stroke-width="1" fill="none"/></svg>Aostrud exerci tation ullam</li>
  </ul>
  <ul class="abs ticks" style="left:224px">
    <li><svg width="8" height="8"><circle cx="4" cy="4" r="4" fill="#1565b4"/><path d="M3 2.2 5 4 3 5.8" stroke="#fff" stroke-width="1" fill="none"/></svg>Lorem ipsum dolor sit amet</li>
    <li><svg width="8" height="8"><circle cx="4" cy="4" r="4" fill="#1565b4"/><path d="M3 2.2 5 4 3 5.8" stroke="#fff" stroke-width="1" fill="none"/></svg>Consectetuer adipiscing</li>
    <li><svg width="8" height="8"><circle cx="4" cy="4" r="4" fill="#1565b4"/><path d="M3 2.2 5 4 3 5.8" stroke="#fff" stroke-width="1" fill="none"/></svg>Pt wisi enim ad</li>
    <li><svg width="8" height="8"><circle cx="4" cy="4" r="4" fill="#1565b4"/><path d="M3 2.2 5 4 3 5.8" stroke="#fff" stroke-width="1" fill="none"/></svg>Aostrud exerci tation ullam</li>
  </ul>
  <div class="abs divider"></div>

  <div class="abs tabs"><span class="tab on">NEWS</span><span class="tab">TWEETS</span><span class="tab">TESTIMONIALS</span></div>
  <div class="abs news">
    <div class="abs news-photo" role="img" aria-label="Hands checking a colour swatch fan against a printed proof"></div>
    <div class="abs news-date">JUL 14</div>
    <div class="abs news-title">Best Printing Ever!</div>
    <p class="abs news-text">Lorem ipsum dolor sit amet, consectetuer adipiscing elit, sed diam nonummy nibh</p>
  </div>
</section>

<footer>
  <div class="abs footer"></div>
  <svg class="abs swoosh" width="753" height="130" viewBox="0 0 753 130">
    <path d="M0 0H753V40C560 102 380 126 250 122C120 118 40 102 0 88Z" fill="#0b4fa0"/>
    <path d="M0 0H753V34C560 94 380 119 250 115C120 111 40 94 0 76Z" fill="#3a8ad6"/>
    <path d="M0 0H753V30C560 90 380 116 250 112C120 108 40 82 0 56Z" fill="#fff"/>
  </svg>
  <div class="abs partners">
    <span class="partner">Arcline</span>
    <span class="partner"><i></i>Whitehaven</span>
    <span class="partner"><i></i>Meadowleaf</span>
    <span class="partner"><i></i>Novaris</span>
    <span class="partner"><i></i>Quartex</span>
  </div>

  <div class="abs f-col" style="left:82px;width:86px">
    <div class="f-head">Quick Links</div>
    <ul class="f-links"><li>Home</li><li>About Us</li><li>Our Services</li><li>Support</li><li>Contact</li></ul>
  </div>
  <div class="abs f-col" style="left:206px;width:130px">
    <div class="f-head">Contact Us</div>
    <div class="contact-row"><svg width="9" height="12" viewBox="0 0 9 12"><path d="M4.5 0A4.5 4.5 0 0 0 0 4.5C0 8 4.5 12 4.5 12S9 8 9 4.5A4.5 4.5 0 0 0 4.5 0Z" fill="#fff"/><circle cx="4.5" cy="4.5" r="1.6" fill="#2c2c2c"/></svg><span>123 PG Duis aute irure doloresg rephenderit in voluptate velit</span></div>
    <div class="contact-row"><svg width="10" height="10" viewBox="0 0 10 10"><path d="M2 0 4 2.5 3 4Q4.5 6.5 6 7L7.5 6 10 8 8.5 10Q3 9.5 0 1.5Z" fill="#fff"/></svg><b>123 456 7890</b></div>
    <div class="contact-row"><svg width="10" height="10" viewBox="0 0 10 10"><rect x="2.5" y="0" width="5" height="3" fill="#fff"/><rect x="0" y="3.5" width="10" height="4" fill="#fff"/><rect x="2.5" y="7" width="5" height="3" fill="#fff"/></svg><b>123 456 7890</b></div>
    <div class="contact-row"><svg width="11" height="8" viewBox="0 0 11 8"><rect width="11" height="8" fill="#fff"/><path d="M0 0 5.5 4.5 11 0" stroke="#2c2c2c" fill="none"/></svg><b style="font-size:7.8px">info@inkvale.com</b></div>
  </div>
  <div class="abs f-col" style="left:375px;width:127px">
    <div class="f-head">Location Map</div>
    <div class="map" role="img" aria-label="Street map showing the company location"></div>
  </div>
  <div class="abs f-col" style="left:543px;width:127px">
    <div class="f-head">Newsletter Sign Up</div>
    <p style="line-height:10.5px">Stay connected and receive email updates from Inkvale</p>
    <div class="field">Enter Your Email</div>
    <div class="submit">SUBMIT</div>
  </div>

  <div class="abs bar"></div>
  <div class="abs copyright">Copyright 2014 Inkvale. All Rights Reserved.</div>
  <div class="abs social" aria-label="Social links"><span></span><span></span><span></span><span></span></div>
</footer>

</body>
</html>
```